Flyer für trilinguale Montessorischule
Zielgruppe
Wir sind eine trilinguale Montessorischule im Herzen der Natur und möchten einen neuen Flyer gestalten für unsere Zielgruppe (Eltern mit Kindern von3-12 Jahren)
Aufgabenstellung
Wichtig ist, dass die Angaben auf französisch und englisch angegegen werden - gerne ein 2-seitiger Flyer. Unser Logo, Design unseres Schulbusses etc. hänge ich unten an. Wichtig ist, in dem Rahmen zu arbeiten. Keywords sind auf dem Bus gut herausgearbeitet.
Wir sind eine familiäre Montessori Schule, die das Kind ins Zentrum setzt. We love what we do. Unsere qualitativ hochwertige Arbeit wird von gut ausgebildeten Lehrkräften liebevoll durchgeführt. Es gibt immer 2 Lehrkräfte in der Klasse (FR, EN und ab 6 Jahren auch noch deutsch dazu).
Details über die Schule:
We believe in teaching new skills in a child-centered way. We provide space for discovery and for opening up to others. Operated by parents and fueled by a strong sense of community our school provides highest quality Montessori education for children aged 3 to 12, a bilingual approach (English & French) for the younger age group, a trilingual approach (English, French and German) for the older age group, freshly-prepared meals, full-day care and free scheduled transportation.
Nous croyons en l'enseignement de nouvelles compétences de manière centrée sur l'enfant. Nous offrons un espace pour la découverte et pour s'ouvrir aux autres. Géré par des parents et alimenté par un fort sentiment de communauté, notre école propose une éducation Montessori de la plus grande qualité pour les enfants de 3 à 12 ans, une approche bilingue (anglais et français) pour le groupe d'âge le plus jeune, une approche trilingue (anglais, français et allemand) pour le groupe d'âge le plus âgé, des repas fraîchement préparés, une garde à temps plein et un service de transport gratuit.

```html
<!DOCTYPE html>
<html lang="fr">
<head>
<meta charset="utf-8">
<title>Ecole Montessori Trois Cent Branches – Flyer FR / EN</title>
<link rel="stylesheet" href="https://fonts.googleapis.com/css2?family=Nunito:wght@700;800;900&family=Quicksand:wght@500;600;700&display=swap">
<style>
  :root {
    --stage: #c4c4c4;
    --paper: #ffffff;
    --leaf: #8dbf44;
    --lime: #bdd232;
    --forest: #587a32;
    --ink: #4d6a2c;
    --text: #4a5a35;
    --photo-building-a: #9a7a4c;
    --photo-building-b: #5f6e3a;
    --photo-forest-a: #b8642a;
    --photo-forest-b: #6b5a38;
    --photo-class-a: #d8c4a4;
    --photo-class-b: #b7825a;
  }
  * { margin: 0; padding: 0; box-sizing: border-box; }
  html, body { width: 1200px; height: 1117px; overflow: hidden; background: var(--stage); }
  .canvas { position: relative; width: 1200px; height: 1117px; }

  .flyer-slot { position: absolute; top: 181px; width: 533px; height: 755px; overflow: hidden; }
  .flyer-slot--fr { left: 54px; }
  .flyer-slot--en { left: 613px; }

  .flyer {
    position: absolute; left: 0; top: 0;
    width: 883px; height: 1250px;
    transform: scale(0.6036); transform-origin: 0 0;
    background: var(--paper);
    font-family: "Quicksand", sans-serif;
    color: var(--text);
  }
  .flyer__art { position: absolute; inset: 0; width: 883px; height: 1250px; }

  .contact { position: absolute; color: #fff; font-family: "Nunito", sans-serif; font-weight: 800; font-size: 28px; display: flex; align-items: center; gap: 12px; white-space: nowrap; }
  .contact--web { top: 50px; left: 418px; }
  .contact--place { top: 108px; left: 502px; }
  .contact svg { width: 34px; height: 34px; flex: none; }

  .brand { position: absolute; left: 44px; top: 166px; display: flex; align-items: center; gap: 34px; }
  .brand__dot { width: 64px; height: 64px; border-radius: 50%; background: var(--leaf); flex: none; }
  .brand__name { font-family: "Quicksand", sans-serif; font-weight: 700; font-size: 35px; line-height: 38px; color: var(--ink); white-space: nowrap; }

  .eco-badge { position: absolute; left: 586px; top: 200px; width: 94px; height: 58px; border: 4px solid var(--forest); border-radius: 10px; }

  .headline { position: absolute; left: 86px; top: 296px; font-family: "Nunito", sans-serif; font-weight: 900; font-size: 68px; line-height: 70px; color: var(--ink); white-space: nowrap; }
  .tagline { position: absolute; left: 86px; font-family: "Nunito", sans-serif; font-weight: 800; font-size: 29px; line-height: 34px; color: var(--leaf); white-space: nowrap; }
  .lead { position: absolute; left: 88px; font-weight: 700; font-size: 18px; line-height: 22px; color: var(--ink); white-space: nowrap; }
  .body-copy { position: absolute; left: 88px; font-weight: 500; font-size: 18px; color: var(--text); white-space: nowrap; }
  .body-copy--fr { top: 630px; line-height: 21.4px; }
  .body-copy--en { top: 646px; line-height: 23.5px; }

  .languages { position: absolute; left: 548px; top: 528px; width: 200px; text-align: center; }
  .languages li { list-style: none; height: 98px; display: flex; flex-direction: column; align-items: center; }
  .languages svg { width: 28px; height: 28px; margin-bottom: 8px; }
  .languages span { font-family: "Nunito", sans-serif; font-weight: 900; font-size: 29px; color: var(--ink); letter-spacing: 0.5px; }
  .age { position: absolute; left: 548px; width: 200px; text-align: center; font-family: "Nunito", sans-serif; font-weight: 900; color: var(--ink); }
  .age--fr { top: 824px; font-size: 42px; line-height: 47px; }
  .age--en { top: 812px; font-size: 38px; line-height: 41px; }
</style>
</head>
<body>
<main class="canvas">

  <!-- French side -->
  <div class="flyer-slot flyer-slot--fr">
    <article class="flyer" lang="fr">
      <svg class="flyer__art" viewBox="0 0 883 1250">
        <defs>
          <linearGradient id="buildingFr" x1="0" y1="0" x2="1" y2="1">
            <stop offset="0" stop-color="var(--photo-building-b)"/>
            <stop offset="1" stop-color="var(--photo-building-a)"/>
          </linearGradient>
          <linearGradient id="classFr" x1="0" y1="0" x2="0" y2="1">
            <stop offset="0" stop-color="var(--photo-class-a)"/>
            <stop offset="1" stop-color="var(--photo-class-b)"/>
          </linearGradient>
        </defs>
        <path fill="var(--leaf)" d="M120,0 H883 V1250 H540 C520,900 540,620 635,370 C560,190 380,50 120,0 Z"/>
        <path fill="var(--lime)" d="M635,370 C700,470 770,700 770,870 C770,1000 760,1100 760,1250 H540 C515,1000 525,650 635,370 Z"/>
        <path fill="var(--forest)" d="M883,65 C780,150 690,270 635,370 C700,470 770,700 770,870 C770,1000 760,1100 883,1200 Z"/>
        <g role="img" aria-label="Photo du bâtiment de l'école entouré d'arbres">
          <path fill="url(#buildingFr)" d="M0,888 H520 C518,1000 525,1120 540,1250 H0 Z"/>
        </g>
        <g role="img" aria-label="Photo d'une fillette souriante à une table de travail Montessori">
          <rect x="540" y="940" width="343" height="310" fill="url(#classFr)"/>
        </g>
      </svg>

      <div class="contact contact--web">
        <svg viewBox="0 0 34 34" fill="none" stroke="var(--forest)" stroke-width="2.2"><circle cx="17" cy="17" r="14"/><ellipse cx="17" cy="17" rx="6" ry="14"/><path d="M3 17h28M5 10h24M5 24h24"/></svg>
        www.troiscentbranches.ch
      </div>
      <div class="contact contact--place">
        <svg viewBox="0 0 34 34"><path fill="var(--forest)" d="M17 2C10 2 5 7 5 13.5 5 22 17 33 17 33S29 22 29 13.5C29 7 24 2 17 2Z"/><circle cx="17" cy="13" r="5" fill="var(--leaf)"/></svg>
        Le Vallon (Arveyres)
      </div>

      <div class="brand">
        <div class="brand__dot"></div>
        <p class="brand__name">Ecole Montessori<br>Trois Cent Branches</p>
      </div>
      <div class="eco-badge"></div>

      <h1 class="headline">école familiale<br>Montessori</h1>
      <p class="tagline" style="top:451px">Nous croyons en l'enseignement<br>de nouvelles compétences<br>de manière centrée sur l'enfant.</p>
      <p class="lead" style="top:576px">Nous offrons un espace pour la découverte<br>et pour s'ouvrir aux autres.</p>
      <p class="body-copy body-copy--fr">Géré par des parents et alimenté par un fort<br>sentiment de communauté, notre école<br>propose une éducation Montessori de la plus<br>haute qualité pour les enfants de 3 à 12 ans,<br>une approche bilingue (anglais et français)<br>pour le groupe d'âge plus jeune, une<br>approche trilingue (anglais, français et<br>allemand) pour le groupe d'âge plus âgé, des<br>repas fraîchement préparés, une garde<br>à temps plein et un transport gratuit sur<br>rendez-vous.</p>

      <ul class="languages">
        <li><svg viewBox="0 0 28 28"><circle cx="14" cy="14" r="13" fill="var(--ink)"/><path d="M8 14.5l4 4 8-8.5" fill="none" stroke="var(--lime)" stroke-width="3" stroke-linecap="round" stroke-linejoin="round"/></svg><span>ANGLAIS</span></li>
        <li><svg viewBox="0 0 28 28"><circle cx="14" cy="14" r="13" fill="var(--ink)"/><path d="M8 14.5l4 4 8-8.5" fill="none" stroke="var(--lime)" stroke-width="3" stroke-linecap="round" stroke-linejoin="round"/></svg><span>FRANÇAIS</span></li>
        <li><svg viewBox="0 0 28 28"><circle cx="14" cy="14" r="13" fill="var(--ink)"/><path d="M8 14.5l4 4 8-8.5" fill="none" stroke="var(--lime)" stroke-width="3" stroke-linecap="round" stroke-linejoin="round"/></svg><span>ALLEMAND</span></li>
      </ul>
      <p class="age age--fr">DE 3 A<br>12 ANS</p>
    </article>
  </div>

  <!-- English side -->
  <div class="flyer-slot flyer-slot--en">
    <article class="flyer" lang="en">
      <svg class="flyer__art" viewBox="0 0 883 1250">
        <defs>
          <linearGradient id="forestEn" x1="0" y1="0" x2="0" y2="1">
            <stop offset="0" stop-color="var(--photo-forest-b)"/>
            <stop offset="1" stop-color="var(--photo-forest-a)"/>
          </linearGradient>
          <linearGradient id="classEn" x1="0" y1="0" x2="0" y2="1">
            <stop offset="0" stop-color="var(--photo-class-a)"/>
            <stop offset="1" stop-color="var(--photo-class-b)"/>
          </linearGradient>
        </defs>
        <path fill="var(--leaf)" d="M120,0 H883 V1250 H540 C520,900 540,620 635,370 C560,190 380,50 120,0 Z"/>
        <path fill="var(--lime)" d="M635,370 C700,470 770,700 770,870 C770,1000 760,1100 760,1250 H540 C515,1000 525,650 635,370 Z"/>
        <path fill="var(--forest)" d="M883,65 C780,150 690,270 635,370 C700,470 770,700 770,870 C770,1000 760,1100 883,1200 Z"/>
        <g role="img" aria-label="Photo of two young children walking hand in hand on a log in an autumn forest">
          <path fill="url(#forestEn)" d="M0,888 H520 C518,1000 525,1120 540,1250 H0 Z"/>
        </g>
        <g role="img" aria-label="Photo of a smiling little girl at a Montessori work table">
          <rect x="540" y="940" width="343" height="310" fill="url(#classEn)"/>
        </g>
      </svg>

      <div class="contact contact--web">
        <svg viewBox="0 0 34 34" fill="none" stroke="var(--forest)" stroke-width="2.2"><circle cx="17" cy="17" r="14"/><ellipse cx="17" cy="17" rx="6" ry="14"/><path d="M3 17h28M5 10h24M5 24h24"/></svg>
        www.troiscentbranches.ch
      </div>
      <div class="contact contact--place">
        <svg viewBox="0 0 34 34"><path fill="var(--forest)" d="M17 2C10 2 5 7 5 13.5 5 22 17 33 17 33S29 22 29 13.5C29 7 24 2 17 2Z"/><circle cx="17" cy="13" r="5" fill="var(--leaf)"/></svg>
        Le Vallon (Arveyres)
      </div>

      <div class="brand">
        <div class="brand__dot"></div>
        <p class="brand__name">Ecole Montessori<br>Trois Cent Branches</p>
      </div>
      <div class="eco-badge"></div>

      <h1 class="headline">family<br>Montessori<br>school</h1>
      <p class="tagline" style="top:509px">We believe in teaching new skills<br>in a child-centered way.</p>
      <p class="lead" style="top:596px">We offer a space for discovery and to<br>open up to others.</p>
      <p class="body-copy body-copy--en">Managed for parents and food for a continued<br>sentiment of the community, our school offers<br>a Montessori education of highest quality for<br>children from 3 to 12 years, a bilingual approach<br>(English and French) for the group of children<br>plus children, A trilingual approach (English,<br>French and German) for the older age group,<br>the freshly prepared meal, full-time care and<br>free transportation by appointment.</p>

      <ul class="languages">
        <li><svg viewBox="0 0 28 28"><circle cx="14" cy="14" r="13" fill="var(--ink)"/><path d="M8 14.5l4 4 8-8.5" fill="none" stroke="var(--lime)" stroke-width="3" stroke-linecap="round" stroke-linejoin="round"/></svg><span>ENGLISH</span></li>
        <li><svg viewBox="0 0 28 28"><circle cx="14" cy="14" r="13" fill="var(--ink)"/><path d="M8 14.5l4 4 8-8.5" fill="none" stroke="var(--lime)" stroke-width="3" stroke-linecap="round" stroke-linejoin="round"/></svg><span>FRENCH</span></li>
        <li><svg viewBox="0 0 28 28"><circle cx="14" cy="14" r="13" fill="var(--ink)"/><path d="M8 14.5l4 4 8-8.5" fill="none" stroke="var(--lime)" stroke-width="3" stroke-linecap="round" stroke-linejoin="round"/></svg><span>GERMAN</span></li>
      </ul>
      <p class="age age--en">FROM<br>3 A 12<br>YEARS</p>
    </article>
  </div>

</main>
</body>
</html>
```